Premium Personal Brand — Facebook Banner (Used Across All Platforms)

Update — Additional Color Direction
In addition to the dark charcoal/slate direction already described, I'm also interested in seeing variants with:
Dark navy blue — Deep, authoritative, intelligence-community feel. Same textured/matte treatment, not flat or bright.
Warm charcoal with steel blue accent — Keep the dark base but introduce a subtle steel blue gradient, accent line, or tonal shift. Sophisticated, modern, adds dimension without adding color noise.
Both should maintain the same premium, restrained, architectural feel described in the original brief. No bright blues, no corporate PowerPoint energy — think midnight, think depth, think weight.
Everything else in the brief remains the same.
I am building a premium personal brand as an executive advisor to founders ($5M+ revenue).
This contest is Facebook-banner–focused, but the design must represent a visual system that will be reused across:
- LinkedIn
- YouTube
I- nstagram
- X (Twitter)
- Website hero sections and other brand touchpoints
Think of the Facebook banner as the primary expression of the brand — not a one-off graphic.
This project is about discovering a high-end visual style and brand feel, not decoration.
What to design
Please submit one cohesive visual system, shown primarily as:
- Facebook banner (primary focus)
The same design language should clearly translate to all platforms listed above.
Designers are responsible for using the current recommended dimensions for each platform.
Quick clarification on background direction:
Backgrounds should have depth and texture, not flat color fields. Avoid pure white, light grey, or solid black backgrounds. Think matte, architectural materials — stone, graphite, concrete, steel — not blank canvases. Subtle tonal variation is encouraged. Obvious gradients or decorative patterns are not.
Text to use
Primary Headline:
- Your Business Is Too Valuable To Be Run On Hope.
Subheadline:
- You didn’t build a business to become its prisoner.
Name:
Paul Whitaker
The headline should be the dominant visual element.
Logo note (important)
My personal logo is currently being finalized.
For this contest:
- Use a simple “PW” monogram placeholder
- Clean, bold, geometric sans-serif
- Do not design a logo
- The winning design must allow an easy logo swap later.
Headshot note (important)
- Please do not include a headshot in the banner design.
- Most platforms display a circular profile image separately.
- The banner should stand on its own using typography, layout, and tone only.
- Design the banner assuming the profile photo will sit nearby, not inside the banner.
Style direction
The design should feel:
- Premium
- Calm
- Confident
- Restrained
- High-trust
- Dark, neutral backgrounds are preferred.
- Fewer elements are better than more.
Think:
- Owner-level advisor
- Private equity / boardroom tone
- Industrial, Modern, Minimalist, Elite, Architectural, not decorative
What to avoid
Please do not submit designs that feel:
- Promotional, hype-driven, or salesy
- Like a coach, guru, or agency
- Bright, colorful, or gradient-heavy
- Busy or over-designed
- Based on stock photos
- No motivational speaker energy.
Reaction test
- If someone sees this banner on Facebook (or later on LinkedIn, YouTube, etc.), the reaction should be:
“That person is serious. I’d trust them with important decisions.”
Final note
- I am not looking for many variations.
- I am looking for one strong visual direction you believe in.
Simple beats clever.
- Restraint beats decoration.

```html
<!DOCTYPE html>
<html lang="en">
<head>
<meta charset="utf-8">
<title>Profile Banner</title>
<link rel="stylesheet" href="https://fonts.googleapis.com/css2?family=Lexend:wght@300;600&family=Barlow:wght@700&display=swap">
<style>
  :root {
    --page-bg: #f4f4f4;
    --stone-dark: #232427;
    --stone-mid: #3a3b3f;
    --stone-light: #55575c;
    --text-light: #ffffff;
    --text-soft: #f1f1f1;
    --name-ink: #111111;
    --avatar-bg: #050505;
  }
  * { margin: 0; padding: 0; box-sizing: border-box; }
  html, body {
    width: 1200px;
    height: 736px;
    overflow: hidden;
    background: var(--page-bg);
  }
  .profile {
    position: relative;
    width: 1200px;
    height: 736px;
  }
  .banner {
    position: absolute;
    left: 64px;
    top: 58px;
    width: 1070px;
    height: 411px;
    overflow: hidden;
  }
  .banner-surface {
    position: absolute;
    inset: 0;
    background:
      radial-gradient(ellipse at 78% 20%, rgba(120,122,128,0.35), transparent 55%),
      radial-gradient(ellipse at 20% 85%, rgba(70,72,76,0.4), transparent 60%),
      linear-gradient(125deg, var(--stone-dark) 0%, var(--stone-mid) 45%, var(--stone-light) 75%, var(--stone-mid) 100%);
  }
  .headline {
    position: absolute;
    left: 38px;
    top: 25px;
    font-family: "Lexend", sans-serif;
    font-weight: 600;
    font-size: 56px;
    line-height: 65px;
    letter-spacing: 0.9px;
    color: var(--text-light);
    white-space: nowrap;
  }
  .divider {
    position: absolute;
    left: 38px;
    top: 182px;
    width: 288px;
    height: 1.5px;
    background: var(--text-soft);
  }
  .subheadline {
    position: absolute;
    left: 38px;
    top: 218px;
    font-family: "Lexend", sans-serif;
    font-weight: 300;
    font-size: 34px;
    line-height: 46px;
    color: var(--text-soft);
    white-space: nowrap;
  }
  .avatar {
    position: absolute;
    left: 105px;
    top: 483px;
    width: 148px;
    height: 148px;
    border-radius: 50%;
    background: radial-gradient(circle at 50% 45%, #6b5548 0%, #2b2626 38%, var(--avatar-bg) 65%);
  }
  .monogram {
    position: absolute;
    left: 274px;
    top: 514px;
    font-family: "Barlow", sans-serif;
    font-weight: 700;
    font-size: 50px;
    line-height: 50px;
    color: var(--name-ink);
  }
</style>
</head>
<body>
  <div class="profile">
    <section class="banner">
      <div class="banner-surface" role="img" aria-label="Dark slate stone texture with diagonal cracks"></div>
      <h1 class="headline">Your Business Is Too Valuable<br>To Be Run On Hope</h1>
      <div class="divider"></div>
      <p class="subheadline">You didn’t build a business<br>to become its prisoner.</p>
    </section>
    <div class="avatar" role="img" aria-label="Circular profile photo placeholder"></div>
    <div class="monogram">PW</div>
  </div>
</body>
</html>
```